Research project presentation flyer

Pending approval of a cooperative research project we need a flyer to present and "market" the academic project to the businesses we want to invite to participate.

The project is a cooperation between three different universities and businesses in the Nordic/Baltic countries and the subject is innovation and entrepreneurship (see the attached "raw" edition).

The intended audience will be all those directly involved with the project, media, municipalities/government, businesses and also the public.

The flyer needs to be in multiple language-editions, but the design must of course be identical. For this designproject, we submit the English content (please correct the English in the attached proposal as necessary). Thus the project result must be in a format that allows us to replace the English text with other languages ourselves.

The proposal attached is just that: a laymans proposal (and the content). Please feel free to rearrange content (and redesign!)

The format of the flyer is a folded A4 (i.e. A5 portrait), with print on both sides.

The raw edition that is attached contains a map that is merely a suggestion (low quality). A better map - perhaps with less irrelevant detail - must be proposed. The important part of the map is to show the location of the universities and project office.

Also, the "logo" of the project is of low quality, and must be changed. A core concept of the project is "triple helix", so the "logo" of the project should be something to that effect (triple helix), as indicated. The "logo" is only an illustration to be used on the flyer. The aim is not to develop a logo for the project. We will do that at a later stage.

The flyer is supposed to be downloadable from a project web, both in hi-res for printing in a professional printshop, and for printing on an average office colour printer. Designs that bleeds off the paper-edge might therefore be a challenge, as office-printers don't print to the edge of the paper.

Reason: Due to Easter holiday and few submissons.

Printing

• Format: A4 folded once, i.e. A5 portrait
Must be able to alter text in design to produce flyers in other languages that English (i.e. pdf is good for the English version, but editable fileformat must also be submitted)
Map must be improved
Logo must be improved. Concept: triple helix
• Clean, professional design.
Flyer is "selling" an academic project that must appeal to businesses

```html
<!DOCTYPE html>
<html lang="en">
<head>
<meta charset="utf-8">
<title>NordInnova – Innovation and Entrepreneurship for Work Life</title>
<link href="https://fonts.googleapis.com/css2?family=Arimo:ital,wght@0,400;0,700;1,400;1,700&display=swap" rel="stylesheet">
<style>
:root{
  --green:#7c9c2a;
  --green-dark:#5e7a1b;
  --green-light:#e7efd2;
  --navy:#1d3a78;
  --blue-soft:#dde8f5;
  --ink:#222;
  --paper:#fff;
  --bg:#d9d9d9;
}
*{box-sizing:border-box;margin:0;padding:0}
html,body{width:839px;height:1200px;overflow:hidden;background:var(--bg);font-family:"Arimo",Arial,sans-serif;color:var(--ink)}
.sheet{display:grid;grid-template-columns:1fr 1fr;grid-template-rows:1fr 1fr;gap:6px;padding:6px;width:839px;height:1200px}
.panel{background:var(--paper);padding:14px 16px;font-size:8.6px;line-height:1.38;overflow:hidden;display:flex;flex-direction:column}
.band{background:var(--green);color:#fff;font-weight:700;font-style:italic;font-size:13px;padding:5px 10px;margin:0 -16px 8px}
.band.first{margin-top:-14px}
.list p{margin-bottom:5px}
.list b{color:var(--navy)}
p{margin-bottom:6px}
.quote{background:var(--blue-soft);border-left:4px solid var(--navy);padding:8px 10px;font-style:italic;color:var(--navy);margin:4px 0 8px}
/* cover */
.cover{padding:0}
.cover-top{display:flex;align-items:center;gap:14px;padding:26px 22px 18px;background:linear-gradient(180deg,#eef4dc,#fff)}
.mark{width:80px;height:80px;border-radius:50%;background:var(--green)}
.title{font-size:46px;font-weight:700;color:var(--navy);line-height:1}
.subtitle{font-size:13px;color:var(--navy);font-weight:700;margin-top:4px}
.stripe{height:8px;background:var(--green)}
.tagline{font-size:17px;font-style:italic;color:var(--green-dark);text-align:right;padding:30px 22px 0 120px;line-height:1.35}
.cover-foot{margin-top:auto;padding:0 22px 26px}
.apply{font-size:13px;font-weight:700;color:var(--navy);line-height:1.4;width:62%}
.deadline{font-size:9px;margin-top:14px}
.cover-row{display:flex;justify-content:space-between;align-items:flex-end}
.partner-badge{width:96px;height:46px;background:var(--green-light);border:1px solid var(--green)}
/* board */
.board h4{font-size:9px;color:var(--navy);margin:4px 0 3px}
.board p{margin-bottom:2px}
.links{color:var(--navy);font-weight:700;margin:4px 0 8px}
/* partners */
.partners-table{border-collapse:collapse;width:100%;font-size:8.6px;margin-bottom:10px}
.partners-table td{padding:3px 4px;vertical-align:top;border-bottom:1px solid #e2e2e2}
.partners-table td:first-child{font-weight:700;color:var(--navy);width:62px}
.map{flex:1;background:linear-gradient(160deg,#bcd4ec 0%,#cfe1b3 55%,#a9c8e6 100%);border:1px solid #9fb4cc;position:relative;margin-bottom:8px}
.map-caption{text-align:center;font-size:9px;font-weight:700;color:var(--navy);margin-bottom:8px}
.logos{display:flex;justify-content:space-around;align-items:center}
.logos span{width:58px;height:58px;border-radius:50%;background:var(--green-light);border:1px solid var(--green)}
</style>
</head>
<body>
<div class="sheet">

  <section class="panel">
    <div class="band first">Project activities – Project language: English</div>
    <div class="list">
      <p><b>WP 01:</b> Project administration, progress and economic control, information and reporting.</p>
      <p><b>WP 02:</b> Development and support of the project web portal.</p>
      <p><b>WP 03:</b> Analysis and development of the concept "Innovation and Entrepreneurship" (IE) within the partner institutions and the work practice within the involved innovation centres. Cooperation with trade/industry and governmental organisations through innovation centres or corresponding organisations for knowledge transfer with work life. Development of differentiated courses within IE – and testing of these.</p>
      <p><b>WP 04:</b> Dissemination of project results and experiences. Producing printed material on project results and experiences, presentation of results at international conferences. Concluding international conference in the final year of the project.</p>
      <p><b>WP 05:</b> Evaluation.</p>
    </div>
    <div class="band">Triple Helix-konseptet</div>
    <p>Internationally, the symbolism of Triple Helix (taken from mathematic models on DNA research) has been introduced in the description of a dynamic process within innovation – illustrating how regions can interact with work life, libraries and change each other in balance. From this the following statement has been presented:</p>
    <div class="quote">"The triple helix concept (three basic elements: (1) a more prominent role for the university in innovation, on a par with industry and government in a knowledge-based society; (2) a movement toward collaborative relationships among the three major institutional spheres, in which innovation policy is increasingly an outcome of interaction rather than a prescription from government; (3) in addition to fulfilling their traditional functions, each institutional sphere also 'takes the role of the other', performing new roles as well as their own traditional function. Institutions taking non-traditional roles are viewed as a major potential source of innovation in innovation."</div>
  </section>

  <section class="panel cover">
    <div class="cover-top">
      <div class="mark"></div>
      <div>
        <div class="title">NordInnova</div>
        <div class="subtitle">Innovation and Entrepreneurship<br>for Work Life</div>
      </div>
    </div>
    <div class="stripe"></div>
    <div class="tagline">A Nordic-Baltic cooperative project on the development of innovation and entrepreneurship in a synthesis between education, trade/industry and governmental organisations.</div>
    <div class="cover-foot">
      <div class="cover-row">
        <div>
          <div class="apply">Application to the Nordlink programme: Nordlink Horizontal, through "Nordic Agency for Education Exchange, NAEE"</div>
          <div class="deadline">Application deadline: 1st March<br>Answer: 1st June</div>
        </div>
        <div class="partner-badge"></div>
      </div>
    </div>
  </section>

  <section class="panel board">
    <div class="band first">Fjellvik Innovation Centre Ltd</div>
    <p>The vision of Fjellvik Innovation Centre is to contribute an important environment for established enterprises and entrepreneurs within "Innovation and Entrepreneurship" in Fjellvik Municipality and the surrounding region with emphasis on high competence within the establishment. The activities and working methods shall create interest regionally, nationally and internationally and the environment and network created shall be visible and contribute to sustainable development in society. The identity and content will be local with global networks and competence.</p>
    <h4>THE BOARD</h4>
    <p>Harald Bekken, Industry networks, Fjellvik Ltd. Chairman of the board</p>
    <p>Sigrid Holmvik, Local administration, Fjellvik</p>
    <p>Tore Lindgaard, Public relations, Regional business office</p>
    <p>Ingrid Fossum, Research coordinator, Elvheim University College</p>
    <div class="links">www.fjellvik-ic.example<br>www.nordinnova.example</div>
    <div class="band">NordInnova <span style="font-weight:400">– Innovation and Entrepreneurship for Work Life</span></div>
    <p>NordInnova – Innovation and Entrepreneurship for Work Life – is a Nordic-Baltic project in cooperation between Fjellvik Innovation Centre Ltd, Elvheim University College, Rivermouth University and Kalda University. The project aims to strengthen the practice and links between innovation and entrepreneurship within higher education, enterprise and governmental organisations in the Nordic countries and the Baltic states.</p>
    <p>Many regions in these countries face great challenges within competence and trade/industry development. These challenges cannot be solved by single organisations alone, but demand innovative processes across several environments and a new way of working together.</p>
    <p>The project plans for transfer between all partners, who will exchange students, teachers and work life contacts, and test a model for new courses. Local and regional innovation centres will coordinate important material and help the dissemination of results to trade/industry around the world.</p>
  </section>

  <section class="panel">
    <div class="band first">Partners</div>
    <table class="partners-table">
      <tr><td>Norway</td><td>Fjellvik Innovation Centre – Project coordinating organisation<br>Elvheim University College<br>Department of Business and Economics</td></tr>
      <tr><td>Estonia</td><td>Kalda University – School of Technology and Business Studies</td></tr>
      <tr><td>Latvia</td><td>Rivermouth University – Institute of Information Studies</td></tr>
    </table>
    <div class="map" role="img" aria-label="Simplified map of the Nordic and Baltic region marking the project office and the three partner universities"></div>
    <div class="map-caption">Fjellvik Innovation Centre</div>
    <div class="logos"><span></span><span></span><span></span></div>
  </section>

</div>
</body>
</html>
```